Infographic & Data Visualisation Design for – Australia’s Yearly Harmwatch Review 2026

About Callowmere Institute: Callowmere Institute is an independent non-profit public health organization. We produce Australia’s Yearly Harmwatch Review, which translates verified national mortality data into actionable insights for policymakers, journalists, healthcare workers, and the general public.

Project Goal: We need a suite of high-impact, clean, and authoritative infographics and data visualisations created for Australia’s Yearly Harmwatch Review 2026.

What We Are Providing:

Full Dataset (.xlsx): Complete Excel file containing all 2026 report data.

Data & Chart Guidance Doc (.docx): A summary document detailing each dataset, the core takeaway, and our initial recommendations for chart types (e.g., line graphs, horizontal bar charts, donut charts, metric tiles).

Callowmere Institute Brand Book (.pdf): Complete brand guidelines covering fonts, colors, line weights, and imagery. These guidelines and in particular colours should be used across the infographics.

Previous Year Reference: You can view how last year’s report and graphics here: https://www.callowmere-example.org.au/australias-yearly-harmwatch-review-2025/

Designer Input & Creative Freedom: While we have provided a guide suggesting specific chart types for each dataset, we are not data visualisation experts - you are! We are very open to your creative ideas, structural suggestions, and design expertise. If you identify a clearer, more engaging, or visually compelling way to illustrate a specific dataset, we welcome your input.

Required Deliverables:

Master Report Infographics: High-resolution, print/PDF-ready A4 vector graphics for the formal report publication (Delivered as vector AI/EPS and high-res PDF/PNG).

Web Assets: Web-optimized PNG/SVG files with transparent or brand backgrounds.

Social Media Adaptations: 1:1 (Square) and 4:5 / 9:16 (Vertical) graphic cards for Instagram, LinkedIn, Facebook, and X.
Updates

Deadline was too tight - have extended it to ensure the designers have enough time to do the job.

Target Market(s)

Policy makers, journalists, health sector professionals, frontline workers, and the general public.

Industry/Entity Type

Drug/Government/Not for Profit

Font styles to use
Sans Serif
Other font styles liked:
• Brand Fonts: Use any or a combination of: Host Grotesk or Libre Baskerville or Poppins or Calibri Light

Colors

Designer to choose colors to be used in the design.

Requirements
Must have
• The ability to create Infographics, graphs of all kinds from data that we have given.
Nice to have
• Help with choosing what infographics/graphs/donuts graphs etc will be best to visualise the data.
Should not have
• A designer who has not made graphs or infographics from Data.

```html
<!DOCTYPE html>
<html lang="en">
<head>
<meta charset="utf-8">
<title>Australia’s Yearly Harmwatch Review 2026</title>
<link rel="stylesheet" href="https://fonts.googleapis.com/css2?family=Barlow+Condensed:wght@500;600;700&family=Barlow:wght@400;500;600&display=swap">
<style>
:root{
  --navy:#0c1e3b;
  --navy-2:#14355a;
  --teal:#13908b;
  --teal-soft:#c7e5e3;
  --purple:#4a2c8c;
  --ink:#1b2433;
  --muted:#5c6676;
  --line:#d9dee4;
  --white:#ffffff;
}
*{margin:0;padding:0;box-sizing:border-box}
html,body{width:800px;height:1200px;overflow:hidden;background:var(--white)}
body{font-family:"Barlow",Arial,sans-serif;color:var(--ink)}
.canvas{position:relative;width:800px;height:1200px;overflow:hidden;background:var(--white)}
.abs{position:absolute}
.cond{font-family:"Barlow Condensed","Arial Narrow",sans-serif}

.side-panel{left:0;top:0}
.brand{left:30px;top:38px;display:flex;align-items:center;gap:10px;color:var(--white)}
.brand-mark{width:32px;height:32px;border:2px solid var(--white)}
.brand-name{font-size:14px;letter-spacing:1.6px;line-height:17px;font-weight:500;text-transform:uppercase}
.pillar{left:30px;display:flex;align-items:center;gap:14px;color:var(--white);font-size:10.5px;font-weight:500;line-height:13px;text-transform:uppercase}
.pillar svg{width:26px;height:26px}
.pillar-rule{left:30px;width:85px;height:1px;background:rgba(255,255,255,.3)}

.title{left:227px;top:28px;font-size:55px;line-height:54px;font-weight:700;color:var(--navy);text-transform:uppercase;letter-spacing:.5px}
.title-rule{left:227px;top:208px;width:37px;height:3px;background:var(--teal)}
.intro{left:192px;top:230px;width:300px;font-size:12px;line-height:23px;color:var(--ink);text-align:center}

.map-title{left:520px;top:222px;font-size:11px;font-weight:600;color:var(--navy);letter-spacing:.3px}
.map-title span{font-size:9px}
.map-sub{left:520px;top:240px;font-size:8.5px;color:var(--muted)}
.map-area{left:486px;top:318px;width:228px;height:252px;border-radius:38% 44% 30% 40% / 34% 40% 38% 44%;background:linear-gradient(135deg,var(--teal-soft) 0%,#9fd2cf 45%,#1a7f80 100%)}
.state{font-size:8.5px;font-weight:600;line-height:12px;color:var(--navy);text-transform:uppercase}
.state-val{font-size:20px;font-weight:500;color:var(--teal);font-family:"Barlow Condensed","Arial Narrow",sans-serif}
.leaders{left:0;top:0;pointer-events:none}

.badge{left:19px;top:346px}
.headline-num{left:145px;top:292px;font-size:180px;line-height:176px;font-weight:600;color:var(--teal);letter-spacing:-3px;transform:scaleX(.8);transform-origin:left top;white-space:nowrap}
.headline-text{left:147px;top:464px;font-size:28px;line-height:34px;font-weight:500;color:var(--navy)}
.headline-text em{font-style:normal;color:var(--teal)}
.source-line{left:147px;top:549px;width:257px;display:flex;align-items:center;gap:10px;font-size:9px;font-weight:500;color:var(--navy);letter-spacing:.3px}
.source-line i{flex:1;height:1px;background:var(--navy)}

.rate-box{left:35px;top:625px;width:735px;height:126px;border:1px solid var(--line);border-radius:12px;box-shadow:0 2px 6px rgba(12,30,59,.06)}
.rate-divider{top:648px;width:1px;height:82px;background:var(--line)}
.rate{top:648px;width:140px;text-align:center;color:var(--navy)}
.rate-label{font-size:12px;font-weight:500;letter-spacing:.2px}
.rate-num{font-size:56px;line-height:54px;font-weight:600;margin-top:2px}
.rate-unit{font-size:12px;font-weight:500;margin-top:2px}

.subs{left:35px;top:770px;width:328px;height:341px;border:1px solid var(--line);border-radius:10px;overflow:hidden;background:var(--white)}
.subs-head{height:54px;background:var(--navy);color:var(--white);font-size:13px;font-weight:500;line-height:18px;padding:11px 0 0 24px;text-transform:uppercase;letter-spacing:.2px}
.subs-head span{font-size:11px}
.sub-row{position:absolute;left:0;width:328px;height:50px;display:flex;align-items:center}
.sub-rank{position:absolute;left:16px;width:22px;height:22px;border-radius:50%;color:var(--white);font-size:12px;font-weight:600;display:flex;align-items:center;justify-content:center}
.sub-icon{position:absolute;left:58px;width:44px;height:44px;border-radius:50%;background:#e9f2f3;display:flex;align-items:center;justify-content:center}
.sub-name{position:absolute;left:121px;font-size:12.5px;line-height:16px;color:var(--ink)}
.sub-val{position:absolute;right:20px;font-size:24px;font-weight:600}
.sub-rule{position:absolute;left:52px;width:256px;height:1px;background:var(--line)}
.subs-source{position:absolute;left:22px;bottom:9px;font-size:8px;color:var(--ink)}
.subs-source b{font-weight:600}

.insight{left:379px;top:770px;width:391px;height:341px;border-radius:10px;overflow:hidden;background:linear-gradient(160deg,var(--navy-2) 0%,var(--navy) 70%)}
.insight-dots{position:absolute;right:0;top:14px;width:196px;height:138px;background:radial-gradient(ellipse at 60% 45%,rgba(19,144,139,.35),rgba(19,144,139,0) 70%)}
.insight-label{position:absolute;left:26px;top:32px;font-size:15px;font-weight:500;color:var(--teal);letter-spacing:.5px}
.insight-quote{position:absolute;left:24px;top:58px;font-family:"Barlow",Arial,sans-serif;font-size:96px;line-height:80px;font-weight:700;color:var(--teal)}
.insight-head{position:absolute;left:26px;top:118px;font-size:23px;line-height:29px;font-weight:500;color:var(--white)}
.insight-art{position:absolute;left:238px;top:113px;width:110px;height:113px;border-radius:50%;background:radial-gradient(circle,rgba(19,144,139,.45),rgba(19,144,139,.08) 70%)}
.insight-rule{position:absolute;left:26px;top:217px;width:177px;height:2px;background:linear-gradient(90deg,var(--teal),rgba(19,144,139,0))}
.insight-body{position:absolute;left:26px;top:236px;width:240px;font-size:12px;line-height:18.5px;color:#e8eef4}

.footer{left:0;top:1127px;width:800px;height:73px;background:var(--navy);color:var(--white)}
.footer-brand{position:absolute;left:26px;top:24px;display:flex;align-items:center;gap:10px;font-size:10.5px;letter-spacing:.5px;font-weight:500;text-transform:uppercase;white-space:nowrap}
.footer-brand i{width:24px;height:24px;border:2px solid var(--white)}
.footer-rule{position:absolute;top:18px;width:1px;height:37px;background:rgba(255,255,255,.35)}
.footer-tag{position:absolute;left:222px;top:20px;font-size:9.5px;line-height:18px;color:var(--teal);font-weight:500}
.footer-tag span{color:#6fb8b4;font-weight:400}
.footer-note{position:absolute;left:609px;top:20px;font-size:9.5px;line-height:17px;color:#dfe6ee}
</style>
</head>
<body>
<div class="canvas">

  <svg class="abs side-panel" width="210" height="330" viewBox="0 0 210 330">
    <polygon points="0,0 207,0 125,301 0,328" fill="#0c1e3b"/>
  </svg>
  <div class="abs brand"><i class="brand-mark"></i><div class="brand-name">Callowmere<br>Institute</div></div>

  <div class="abs pillar" style="top:120px">
    <svg viewBox="0 0 26 26"><path d="M13 2 L23 6 V13 C23 19 18 23 13 24 C8 23 3 19 3 13 V6 Z" fill="none" stroke="#13908b" stroke-width="2"/><path d="M8.5 13 L12 16.5 L18 10" fill="none" stroke="#13908b" stroke-width="2"/></svg>
    <span>Evidence<br>based</span>
  </div>
  <div class="abs pillar-rule" style="top:168px"></div>
  <div class="abs pillar" style="top:186px">
    <svg viewBox="0 0 26 26"><rect x="2" y="15" width="5" height="9" fill="#13908b"/><rect x="10" y="10" width="5" height="14" fill="#13908b"/><rect x="18" y="4" width="5" height="20" fill="#13908b"/></svg>
    <span>Data<br>driven</span>
  </div>
  <div class="abs pillar-rule" style="top:228px"></div>
  <div class="abs pillar" style="top:245px">
    <svg viewBox="0 0 26 26"><circle cx="8" cy="8" r="4" fill="#13908b"/><circle cx="18" cy="8" r="4" fill="#13908b"/><rect x="2" y="14" width="11" height="9" rx="4" fill="#13908b"/><rect x="13" y="14" width="11" height="9" rx="4" fill="#13908b"/></svg>
    <span>Action<br>focused</span>
  </div>

  <h1 class="abs title cond">Australia’s<br>Yearly Harmwatch<br>Review 2026</h1>
  <div class="abs title-rule"></div>
  <p class="abs intro">Drug-induced deaths remain one of Australia’s most significant preventable public health challenges.</p>

  <div class="abs map-title">DEATHS BY STATE &amp; TERRITORY <span>(2024)</span></div>
  <div class="abs map-sub">Drug-induced deaths occur in every part of Australia.</div>
  <div class="abs map-area" role="img" aria-label="Map of Australia shaded by number of drug-induced deaths per state and territory"></div>

  <svg class="abs leaders" width="800" height="620" viewBox="0 0 800 620" fill="none" stroke="#0c1e3b" stroke-width="1">
    <path d="M574 310 V355"/>
    <circle cx="574" cy="355" r="2.5" fill="#0c1e3b"/>
    <path d="M465 396 H490 L512 420"/><circle cx="512" cy="420" r="2.5" fill="#0c1e3b"/>
    <path d="M717 339 H693 L672 368"/><circle cx="672" cy="368" r="2.5" fill="#0c1e3b"/>
    <path d="M735 425 L690 447"/><circle cx="690" cy="447" r="2.5" fill="#0c1e3b"/>
    <path d="M730 491 H695 L680 494"/><circle cx="678" cy="495" r="3" fill="#fff"/>
    <path d="M732 545 H708 L666 518"/><circle cx="664" cy="517" r="2.5" fill="#0c1e3b"/>
    <path d="M617 586 H640 L656 570"/>
    <path d="M498 528 H521 L544 503"/><circle cx="545" cy="502" r="2.5" fill="#0c1e3b"/>
  </svg>

  <div class="abs state" style="left:565px;top:267px;text-align:center">Northern<br>Territory</div>
  <div class="abs state-val" style="left:576px;top:290px">15</div>
  <div class="abs state" style="left:427px;top:362px">Western<br>Australia</div>
  <div class="abs state-val" style="left:427px;top:384px">278</div>
  <div class="abs state" style="left:717px;top:317px">Queensland</div>
  <div class="abs state-val" style="left:718px;top:326px">417</div>
  <div class="abs state" style="left:737px;top:395px">New South<br>Wales</div>
  <div class="abs state-val" style="left:737px;top:418px">587</div>
  <div class="abs state" style="left:733px;top:468px">Australian<br>Capital<br>Territory</div>
  <div class="abs state-val" style="left:733px;top:503px">29</div>
  <div class="abs state" style="left:730px;top:539px">Victoria</div>
  <div class="abs state-val" style="left:734px;top:549px">572</div>
  <div class="abs state" style="left:569px;top:570px">Tasmania</div>
  <div class="abs state-val" style="left:584px;top:580px">35</div>
  <div class="abs state" style="left:447px;top:510px">South<br>Australia</div>
  <div class="abs state-val" style="left:447px;top:533px">157</div>

  <svg class="abs badge" width="118" height="118" viewBox="0 0 118 118">
    <circle cx="59" cy="59" r="59" fill="#f1f4f6"/>
    <circle cx="59" cy="59" r="51" fill="#fff" stroke="#13908b" stroke-width="3"/>
    <circle cx="59" cy="59" r="20" fill="#13908b" role="img" aria-label="Community group icon"/>
  </svg>
  <div class="abs headline-num cond">2,596</div>
  <div class="abs headline-text cond">Australians lost their lives<br>to <em>drug-induced</em> causes</div>
  <div class="abs source-line"><i></i>2024 NATIONAL MORTALITY DATA<i></i></div>

  <div class="abs rate-box"></div>
  <div class="abs rate-divider" style="left:289px"></div>
  <div class="abs rate-divider" style="left:517px"></div>

  <svg class="abs" style="left:70px;top:650px" width="64" height="70" viewBox="0 0 64 70" fill="none" stroke="#13908b" stroke-width="2.5">
    <rect x="2" y="8" width="60" height="58" rx="6"/><path d="M2 22 H62 M16 2 V13 M48 2 V13"/>
    <g fill="#13908b" stroke="none"><rect x="13" y="32" width="7" height="7"/><rect x="28" y="32" width="7" height="7"/><rect x="43" y="32" width="7" height="7"/><rect x="13" y="48" width="7" height="7"/><rect x="28" y="48" width="7" height="7"/><rect x="43" y="48" width="7" height="7"/></g>
  </svg>
  <div class="abs rate cond" style="left:134px"><div class="rate-label">EVERY WEEK</div><div class="rate-num" style="color:#13908b">50</div><div class="rate-unit">DEATHS</div></div>

  <svg class="abs" style="left:315px;top:652px" width="72" height="72" viewBox="0 0 72 72" fill="none" stroke="#4a2c8c" stroke-width="2.5">
    <circle cx="36" cy="36" r="34"/><path d="M36 14 V36 L48 48"/>
  </svg>
  <div class="abs rate cond" style="left:375px"><div class="rate-label">EVERY DAY</div><div class="rate-num" style="color:#4a2c8c">7</div><div class="rate-unit">DEATHS</div></div>

  <svg class="abs" style="left:544px;top:648px" width="66" height="74" viewBox="0 0 66 74" fill="none" stroke="#13908b" stroke-width="2.5">
    <circle cx="33" cy="42" r="29"/><path d="M27 3 H39 M33 3 V13 M55 16 L59 12 M33 42 V26 M33 42 H44"/>
    <circle cx="33" cy="42" r="2.5" fill="#13908b"/>
  </svg>
  <div class="abs rate cond" style="left:617px"><div class="rate-label">EVERY 3.5 HOURS</div><div class="rate-num" style="color:#13908b">1</div><div class="rate-unit">DEATH</div></div>

  <section class="abs subs">
    <div class="subs-head">Leading substances involved in<br>unintentional overdose deaths <span>(2024)</span></div>

    <div class="sub-row" style="top:60px">
      <div class="sub-rank" style="background:#13908b">1</div>
      <div class="sub-icon"><svg width="26" height="26" viewBox="0 0 26 26"><rect x="2" y="8" width="22" height="10" rx="5" transform="rotate(-40 13 13)" fill="none" stroke="#13908b" stroke-width="2"/><path d="M9 17 L17 9" stroke="#13908b" stroke-width="2"/></svg></div>
      <div class="sub-name">Opioids</div><div class="sub-val cond" style="color:#13908b">877</div>
    </div>
    <div class="sub-rule" style="top:110px"></div>
    <div class="sub-row" style="top:111px">
      <div class="sub-rank" style="background:#13908b">2</div>
      <div class="sub-icon"><svg width="24" height="24" viewBox="0 0 24 24"><path d="M12 2 L20 8 L17 21 H7 L4 8 Z" fill="none" stroke="#13908b" stroke-width="1.8"/></svg></div>
      <div class="sub-name">Amphetamine-type<br>stimulants</div><div class="sub-val cond" style="color:#13908b">772</div>
    </div>
    <div class="sub-rule" style="top:161px"></div>
    <div class="sub-row" style="top:161px">
      <div class="sub-rank" style="background:#4a2c8c">3</div>
      <div class="sub-icon"><svg width="26" height="26" viewBox="0 0 26 26"><circle cx="13" cy="13" r="10" fill="none" stroke="#4a2c8c" stroke-width="2"/><path d="M6 20 L20 6" stroke="#4a2c8c" stroke-width="2"/></svg></div>
      <div class="sub-name">Benzodiazepines</div><div class="sub-val cond" style="color:#4a2c8c">514</div>
    </div>
    <div class="sub-rule" style="top:211px"></div>
    <div class="sub-row" style="top:211px">
      <div class="sub-rank" style="background:#13908b">4</div>
      <div class="sub-icon"><svg width="20" height="28" viewBox="0 0 20 28"><rect x="7" y="1" width="6" height="5" fill="none" stroke="#13908b" stroke-width="1.8"/><rect x="3" y="8" width="14" height="19" rx="3" fill="none" stroke="#13908b" stroke-width="1.8"/><rect x="6" y="14" width="8" height="6" fill="#13908b"/></svg></div>
      <div class="sub-name">Alcohol</div><div class="sub-val cond" style="color:#13908b">311</div>
    </div>
    <div class="sub-rule" style="top:262px"></div>
    <div class="sub-row" style="top:262px">
      <div class="sub-rank" style="background:#4a2c8c">5</div>
      <div class="sub-icon" role="img" aria-label="Mental health icon"></div>
      <div class="sub-name">Antidepressants</div><div class="sub-val cond" style="color:#4a2c8c">293</div>
    </div>
    <div class="subs-source"><b>Source:</b> NSO National Mortality Database (2024).</div>
  </section>

  <section class="abs insight">
    <div class="insight-dots" role="img" aria-label="Faint dotted pattern of the Australian continent"></div>
    <div class="insight-label cond">KEY INSIGHT</div>
    <div class="insight-quote">“</div>
    <div class="insight-head cond">More Australians die<br>from drug-induced causes<br>than many people realise.</div>
    <div class="insight-art" role="img" aria-label="Illustration of open hands supporting a group of people"></div>
    <div class="insight-rule"></div>
    <p class="insight-body">The burden is experienced across every state and territory, highlighting the need for evidence-based prevention, treatment and harm reduction responses.</p>
  </section>

  <footer class="abs footer">
    <div class="footer-brand"><i></i>Callowmere Institute</div>
    <div class="footer-rule" style="left:207px"></div>
    <div class="footer-tag">INDEPENDENT. EVIDENCE-BASED. ACTION-FOCUSED.<br><span>callowmere-example.org.au</span></div>
    <div class="footer-rule" style="left:594px"></div>
    <div class="footer-note">Building a healthier Australia<br>through evidence and action.</div>
  </footer>

</div>
</body>
</html>
```